Business Card design

We have found an idea we would like to do something similar.
We would require the cards for the inside and the wrapping sheet for the outside, you will see what I mean when you see the image attached. (gum packet) The company is called.... Tallowmere Swift Press
I will include the company logo also.
If you could create the outside wrapping with the ability to have staff members name and mobile, maybe on one side panel we would have the address, the other side would be phone numbers, the front would be staff members name and mobile number and email. The other side would be company name and logo if it fits, the logo could wrap around if needed. Open to all ideas.

```html
<!DOCTYPE html>
<html lang="en">
<head>
<meta charset="utf-8">
<title>Tallowmere Swift Press – Business Stick Wrapper and Cards</title>
<link rel="stylesheet" href="https://fonts.googleapis.com/css2?family=Questrial&family=Anton&display=swap">
<style>
  :root {
    --wrap-yellow: #f6e61c;
    --wrap-yellow-deep: #efd80f;
    --silver-light: #f4f4f4;
    --silver-mid: #c9c9c9;
    --silver-dark: #8e8e8e;
    --card-beige: #e5d4b5;
    --ink: #1d1d1b;
    --accent-orange: #ee7a3b;
    --accent-red: #d8351f;
    --label-white: #ffffff;
    --page: #ffffff;
  }
  * { box-sizing: border-box; margin: 0; padding: 0; }
  html, body { width: 1200px; height: 1000px; overflow: hidden; background: var(--page); }
  body { font-family: "Questrial", sans-serif; color: var(--ink); position: relative; }

  /* ---------- wrapper sheet ---------- */
  .wrapper {
    position: absolute; left: 60px; width: 1080px; height: 290px;
    display: flex; box-shadow: 0 6px 18px rgba(0,0,0,.18);
  }
  .wrapper--company { top: 40px; }
  .wrapper--staff { top: 360px; }
  .wrapper__foil {
    width: 70px; height: 100%;
    background: linear-gradient(90deg, var(--silver-dark), var(--silver-light) 35%, var(--silver-mid) 60%, var(--silver-light) 80%, var(--silver-dark));
  }
  .wrapper__body { flex: 1; display: flex; flex-direction: column; }
  .wrapper__top, .wrapper__front {
    position: relative;
    background: radial-gradient(circle at 30% 40%, var(--wrap-yellow) 0%, var(--wrap-yellow-deep) 100%);
  }
  .wrapper__top { height: 120px; border-bottom: 1px solid rgba(0,0,0,.12); }
  .wrapper__front { flex: 1; }

  .name-label {
    position: absolute; left: 200px; top: 30px;
    background: var(--label-white); border: 6px solid var(--ink);
    padding: 2px 26px;
    font-family: "Anton", sans-serif; font-size: 44px; letter-spacing: 2px; line-height: 1.1;
  }
  .count {
    position: absolute; right: 40px; top: 30px; text-align: right; line-height: 1;
  }
  .count__num { display: block; font-size: 18px; font-family: "Anton", sans-serif; }
  .count__label { font-size: 12px; }

  .brand-mark {
    position: absolute; left: 60px; top: 50px; display: flex; align-items: center; gap: 12px;
  }
  .brand-mark__dot { width: 56px; height: 56px; border-radius: 50%; background: var(--accent-orange); }
  .brand-mark__name { font-size: 20px; color: var(--accent-red); width: 130px; line-height: 1.2; }

  .company-info { position: absolute; left: 320px; top: 22px; line-height: 1.45; }
  .company-info__name { font-size: 30px; margin-bottom: 6px; }
  .company-info__line { font-size: 17px; }

  .staff-name { position: absolute; left: 60px; top: 22px; font-size: 38px; }
  .staff-role { position: absolute; left: 62px; top: 70px; font-size: 16px; }
  .staff-phone { position: absolute; left: 60px; bottom: 20px; font-size: 22px; }
  .staff-email { position: absolute; right: 50px; bottom: 50px; font-size: 20px; }

  /* ---------- cards ---------- */
  .card {
    position: absolute; top: 700px; width: 500px; height: 250px;
    background: var(--card-beige); box-shadow: 0 5px 14px rgba(0,0,0,.2);
  }
  .card--front { left: 60px; }
  .card--back { left: 640px; display: flex; align-items: center; gap: 22px; padding-left: 40px; }

  .card__brand { position: absolute; left: 28px; top: 70px; width: 130px; text-align: center; }
  .card__brand-dot { width: 70px; height: 70px; margin: 0 auto 10px; border-radius: 50%; background: var(--accent-orange); }
  .card__brand-name { font-size: 15px; color: var(--ink); line-height: 1.2; }

  .card__name { position: absolute; left: 180px; top: 40px; font-size: 24px; }
  .card__role { position: absolute; left: 184px; top: 72px; font-size: 13px; }
  .card__email { position: absolute; right: 26px; top: 74px; font-size: 13px; }
  .card__phone { position: absolute; left: 184px; top: 112px; font-size: 14px; }
  .card__rule { position: absolute; left: 180px; right: 26px; top: 136px; border-top: 1px solid var(--ink); }
  .card__address { position: absolute; left: 184px; top: 148px; font-size: 13px; line-height: 1.5; }
  .card__web { position: absolute; right: 26px; top: 178px; font-size: 13px; }

  .card__back-dot { width: 90px; height: 90px; border-radius: 50%; background: var(--accent-orange); flex: none; }
  .card__back-name { font-size: 28px; color: var(--accent-orange); }
</style>
</head>
<body>

  <!-- Company wrapper: label top, company details front -->
  <section class="wrapper wrapper--company">
    <div class="wrapper__foil"></div>
    <div class="wrapper__body">
      <div class="wrapper__top">
        <div class="name-label">SAMPLE NAME</div>
        <div class="count"><span class="count__num">20</span><span class="count__label">Business Stick</span></div>
      </div>
      <div class="wrapper__front">
        <div class="brand-mark">
          <div class="brand-mark__dot"></div>
          <div class="brand-mark__name">Tallowmere Swift Press</div>
        </div>
        <div class="company-info">
          <p class="company-info__name">Tallowmere Swift Press</p>
          <p class="company-info__line">Sample Address, Unit #, City, 12345</p>
          <p class="company-info__line">(00) 123456789</p>
          <p class="company-info__line">www.tallowmereswift.org</p>
        </div>
      </div>
    </div>
    <div class="wrapper__foil"></div>
  </section>

  <!-- Staff wrapper: label top, staff details front -->
  <section class="wrapper wrapper--staff">
    <div class="wrapper__foil"></div>
    <div class="wrapper__body">
      <div class="wrapper__top">
        <div class="name-label">SAMPLE NAME</div>
        <div class="count"><span class="count__num">20</span><span class="count__label">Business Stick</span></div>
      </div>
      <div class="wrapper__front">
        <p class="staff-name">Sample Name</p>
        <p class="staff-role">Your Potition</p>
        <p class="staff-phone">123 456 789</p>
        <p class="staff-email">sample@email.com</p>
      </div>
    </div>
    <div class="wrapper__foil"></div>
  </section>

  <!-- Business card front -->
  <article class="card card--front">
    <div class="card__brand">
      <div class="card__brand-dot"></div>
      <p class="card__brand-name">Tallowmere Swift Press</p>
    </div>
    <p class="card__name">Sample Name</p>
    <p class="card__role">Your Potition</p>
    <p class="card__email">sample@email.com</p>
    <p class="card__phone">123 456 789</p>
    <div class="card__rule"></div>
    <p class="card__address">Sample Address, Unit #, City, 12345<br>(00) 123456789</p>
    <p class="card__web">www.tallowmereswift.org</p>
  </article>

  <!-- Business card back -->
  <article class="card card--back">
    <div class="card__back-dot"></div>
    <p class="card__back-name">Tallowmere Swift Press</p>
  </article>

</body>
</html>
```